Business Card Design

I would like a simple logo for Marwick Holdings.
We run a company that looks after our extended
family's investments.

Industry/Entity Type

Business

Contact Information for Business Card

Colleen Barfoot
Director
Marwick Holdings
ABN 72 318 506 942
Investment Management
colleen@marwickholdings.com.au
Mobile +61 437 880 642
Level 1, 57 Paxton St
Townsville, Qld 4810

```html
<!DOCTYPE html>
<html lang="en">
<head>
<meta charset="utf-8">
<title>Marwick Holdings – Business Card</title>
<link rel="stylesheet" href="https://fonts.googleapis.com/css2?family=Didact+Gothic&family=Open+Sans:wght@400&display=swap">
<style>
  :root {
    --page: #ffffff;
    --card: #cc95c4;
    --band: #ed1c24;
    --navy: #2e3192;
    --ink: #231f20;
    --accent: #fff200;
    --band-text: #ffffff;
  }
  html, body {
    margin: 0;
    padding: 0;
    width: 1200px;
    height: 679px;
    overflow: hidden;
    background: var(--page);
  }
  .business-card {
    display: block;
    width: 1200px;
    height: 679px;
  }
  .card-face { fill: var(--card); }
  .abn-band { fill: var(--band); }
  .brand-mark { fill: none; stroke: var(--navy); stroke-width: 22; }
  .brand-name {
    font-family: "Didact Gothic", sans-serif;
    font-size: 46px;
    fill: var(--navy);
  }
  .brand-tagline {
    font-family: "Didact Gothic", sans-serif;
    font-size: 29px;
    fill: var(--ink);
  }
  .person-name {
    font-family: "Didact Gothic", sans-serif;
    font-size: 49px;
    fill: var(--ink);
  }
  .person-role {
    font-family: "Didact Gothic", sans-serif;
    font-size: 34px;
    fill: var(--accent);
  }
  .contact-line {
    font-family: "Didact Gothic", sans-serif;
    font-size: 30px;
    fill: var(--ink);
  }
  .contact-email {
    font-size: 23px;
    fill: var(--accent);
  }
  .abn-text {
    font-family: "Open Sans", sans-serif;
    font-size: 24px;
    fill: var(--band-text);
  }
</style>
</head>
<body>
  <svg class="business-card" viewBox="0 0 1200 679" xmlns="http://www.w3.org/2000/svg" role="img" aria-label="Marwick Holdings business card for Colleen Barfoot, Director">
    <rect class="card-face" x="23" y="10" width="1155" height="659"/>
    <rect class="abn-band" x="23" y="622" width="1155" height="41"/>

    <g class="brand">
      <circle class="brand-mark" cx="335" cy="292" r="93"/>
      <text class="brand-name" x="345" y="500" text-anchor="middle">Marwick Holdings</text>
      <text class="brand-tagline" x="342" y="546" text-anchor="middle">Investment Management</text>
    </g>

    <g class="person">
      <text class="person-name" x="675" y="252">Colleen Barfoot</text>
      <text class="person-role" x="860" y="298" text-anchor="middle">Director</text>
    </g>

    <g class="contact">
      <text class="contact-line" x="669" y="446">Level 1, 57 Paxton St</text>
      <text class="contact-line" x="669" y="483">Townsville, Qld 4810</text>
      <text class="contact-line" x="675" y="549">Mobile +61 437 880 642</text>
      <text class="contact-line" x="675" y="586">E-mail : <tspan class="contact-email">colleen@marwickholdings.com.au</tspan></text>
    </g>

    <text class="abn-text" x="838" y="654" text-anchor="middle">ABN 72 318 506 942</text>
  </svg>
</body>
</html>
```